Landing Page Design

We need a landing page template designed to support a clients Zenfy Bidpost Campaigns. The client is called Morlet Plumbing and they install and repair hot water systems (only). They provide no other plumbing services.

We are really looking for a great looking landing page that is both engaging and functional.

Target Market(s)

Residential/Domestic market. Typically wives and partners who are typically home or run the household.

Industry/Entity Type

Plumbing

Number of Pages Required

1 page

Requirements
Must have
• Strong branding
Strong call to actions
Great and obvious looking buttons
Nice to have
• Smart use of colour
Should not have
• The design should not use old-style, serif fonts.

Do not include any plumbing images

```html
<!DOCTYPE html>
<html lang="en">
<head>
<meta charset="utf-8">
<title>Morlet Plumbing – Hot Water Systems</title>
<link rel="stylesheet" href="https://fonts.googleapis.com/css2?family=Arimo:wght@400;700&display=swap">
<style>
  :root {
    --orange: #f07f1e;
    --orange-light: #f7a43a;
    --amber: #f6b336;
    --amber-dark: #ef8f1d;
    --green: #5aa83a;
    --green-light: #7cc04f;
    --form-grey: #ececec;
    --field-border: #9a9a9a;
    --ink: #2b2b2b;
    --white: #ffffff;
    --brand-red: #d9342b;
  }
  * { box-sizing: border-box; margin: 0; padding: 0; }
  html, body { width: 1200px; height: 1153px; overflow: hidden; background: var(--white); }
  body { font-family: "Arimo", Arial, sans-serif; color: var(--ink); position: relative; }

  .top-bar {
    position: absolute; left: 0; top: 0; width: 1200px; height: 34px;
    background: linear-gradient(90deg, var(--orange-light), var(--orange));
    color: var(--white); font-size: 15px; padding: 8px 20px;
  }

  .brand {
    position: absolute; left: 42px; top: 230px;
    display: flex; align-items: center; gap: 16px;
  }
  .brand-dot { width: 44px; height: 44px; border-radius: 50%; background: var(--orange); }
  .brand-name { font-size: 50px; font-weight: 700; color: var(--brand-red); letter-spacing: 1px; }

  .promises { position: absolute; left: 930px; top: 182px; width: 228px; list-style: none; }
  .promises li {
    height: 38px; margin-bottom: 9px; border-radius: 4px;
    background: linear-gradient(180deg, var(--amber), var(--amber-dark));
    color: var(--white); font-size: 15px; line-height: 38px; padding-left: 12px;
    box-shadow: 0 2px 3px rgba(0,0,0,0.15);
  }

  .rule { position: absolute; left: 0; top: 514px; width: 1200px; height: 4px; background: var(--orange); }
  .main-nav {
    position: absolute; left: 245px; top: 460px; width: 815px; height: 56px;
    background: linear-gradient(180deg, var(--green-light), var(--green));
    border-radius: 28px 28px 0 0;
    display: flex; align-items: center;
  }
  .main-nav a {
    color: var(--white); font-weight: 700; font-size: 19px; text-decoration: none;
    flex: 1; text-align: center; border-left: 3px solid var(--white); line-height: 22px;
  }
  .main-nav a:first-child { border-left: none; }
  .main-nav a.is-current { color: var(--orange); }

  .services { position: absolute; left: 56px; top: 578px; width: 340px; font-size: 17px; line-height: 1.4; }
  .services h2 { font-size: 20px; font-weight: 400; letter-spacing: 2px; margin-bottom: 22px; }
  .services p { margin-bottom: 22px; }

  .offer-form { position: absolute; left: 413px; top: 538px; width: 420px; height: 524px; background: var(--form-grey); }
  .offer-head {
    background: var(--green); color: var(--white); font-weight: 700;
    text-align: center; font-size: 15px; line-height: 1.4; height: 92px; padding-top: 12px;
  }
  .offer-head .now { color: var(--orange); }
  .offer-body { padding: 8px 22px 0 22px; font-size: 16px; }
  .offer-body label { display: block; margin-top: 4px; line-height: 20px; }
  .field { display: block; width: 100%; height: 20px; border: 1px solid var(--field-border); background: var(--white); }
  .picker {
    margin-top: 4px; width: 150px; height: 26px; border-radius: 13px; border: 1px solid var(--field-border);
    background: linear-gradient(180deg, #fff, #ddd); font-size: 15px; padding: 3px 0 0 24px; position: relative;
  }
  .picker svg { position: absolute; right: 8px; top: 5px; }
  .field-tall { height: 100px; }
  .more-info {
    position: absolute; left: 110px; top: 466px; width: 200px; height: 40px; border-radius: 20px;
    background: linear-gradient(180deg, var(--green-light), var(--green));
    color: var(--white); font-weight: 700; font-size: 19px; text-align: center; line-height: 40px; letter-spacing: 1px;
  }

  .testimonials { position: absolute; left: 880px; top: 580px; width: 290px; font-size: 18px; line-height: 1.3; }
  .testimonials h2, .tips h2 { font-size: 19px; font-weight: 400; letter-spacing: 1px; margin-bottom: 14px; }
  .testimonials h2 b, .tips h2 b { font-weight: 700; }
  .portrait { width: 132px; height: 122px; background: linear-gradient(180deg, #d9d2cb, #8b8582); margin-bottom: 10px; }
  .author { text-align: right; margin-top: 8px; padding-right: 20px; }

  .tips { position: absolute; left: 880px; top: 900px; width: 280px; font-size: 16px; }
  .tips-select {
    margin-top: 8px; width: 262px; height: 42px; border-radius: 21px; border: 1px solid var(--field-border);
    background: linear-gradient(180deg, #fff, #e4e4e4); position: relative; line-height: 42px; text-align: center; padding-right: 36px;
  }
  .tips-select svg { position: absolute; right: 4px; top: 4px; }

  .site-footer {
    position: absolute; left: 0; top: 1062px; width: 1200px; height: 91px;
    background: linear-gradient(90deg, var(--orange), var(--orange-light));
    color: var(--white); font-size: 16px; display: flex; align-items: center;
  }
  .footer-brand { width: 200px; padding-left: 30px; font-weight: 700; font-size: 20px; }
  .footer-links { padding-left: 30px; }
  .footer-links span { margin: 0 14px; }
</style>
</head>
<body>
  <header class="top-bar">www.morletplumbing.com</header>

  <div class="brand">
    <span class="brand-dot"></span>
    <span class="brand-name">Morlet Plumbing</span>
  </div>

  <ul class="promises">
    <li>Sydney 24 Hours 7 Days</li>
    <li>On Time</li>
    <li>Professional Technicians</li>
    <li>We Advise on Rebates</li>
    <li>Authorised Veltra Dealer</li>
  </ul>

  <nav class="main-nav">
    <a href="#">ABOUT US</a>
    <a href="#" class="is-current">SERVICES</a>
    <a href="#">SOLUTIONS</a>
    <a href="#">SUPPORT</a>
    <a href="#">CONTACT</a>
  </nav>
  <div class="rule"></div>

  <section class="services">
    <h2>SERVICES</h2>
    <p>Solar Hot Water Systems</p>
    <p>Engage our routine office cleaning for at least 6 months and receive a FREE Carpet and Window clean! No strings attached, no contracts.</p>
    <p>To take advantage of this great offer call us on 1300 58 41 90 or complete and submit the form on this page.</p>
    <p>At Morlet we provide all your property service needs painlessly. We understand that cleaning and other property services should be background activities. A set and forget proposition.</p>
  </section>

  <form class="offer-form">
    <div class="offer-head">Take advantage of this great offer.<br>Contact Us <span class="now">NOW</span> on 9712 4305<br>or register your interest below</div>
    <div class="offer-body">
      <label>First Name:</label><span class="field"></span>
      <label>Last Name:</label><span class="field"></span>
      <label>Services Type:</label>
      <div class="picker">Select One
        <svg width="18" height="14" viewBox="0 0 18 14"><ellipse cx="9" cy="7" rx="9" ry="7" fill="#f6b336"/><path d="M5 5h8l-4 5z" fill="#b5651d"/></svg>
      </div>
      <label>Best Contact Number:</label><span class="field"></span>
      <label>Email Address:</label><span class="field"></span>
      <label>Enquiry/Comments:</label><span class="field field-tall"></span>
    </div>
    <div class="more-info">MORE INFO</div>
  </form>

  <aside class="testimonials">
    <h2>CLIENT <b>TESTIMONIALS</b></h2>
    <div class="portrait" role="img" aria-label="Photo of a satisfied client"></div>
    <p>"Engage our routine office cleaning for at least 6 months and receive a Carpet and Window clean! No strings attached, no contracts."</p>
    <p class="author">Solar Hot Water Systems</p>
  </aside>

  <aside class="tips">
    <h2>HELPFUL <b>TIPS</b></h2>
    <p>Business/Residential:</p>
    <div class="tips-select">Select One
      <svg width="34" height="34" viewBox="0 0 34 34"><circle cx="17" cy="17" r="16" fill="#5aa83a"/><circle cx="15" cy="15" r="6" fill="none" stroke="#fff" stroke-width="3"/><path d="M19 19l6 6" stroke="#fff" stroke-width="3" stroke-linecap="round"/></svg>
    </div>
  </aside>

  <footer class="site-footer">
    <div class="footer-brand">Morlet Plumbing</div>
    <div class="footer-links">Morlet Plumbing &copy; 2010 Privacy Policy<span>|</span>Terms &amp; Condition<span></span>Contact Phone: 1300 58 41 90</div>
  </footer>
</body>
</html>
```